Professional Website Design to match new logo for Medical Legal Company

We have rebranded our company and We want a professional but also dynamic web site design for a group of esteemed doctors that provide expert evaluation of an injured worker in a Workers Compensation case.
​
1. Our target market is both the attorneys who select our doctors and any doctors who would wish to join our group.

2. Notes for the Landing Page:
- We prefer a simpler, sleeker more modern look for the landing page.
- We want a simplified landing page with one image, three buttons highlighted in Content document.
- We want the main image to be black and white but it can be splashed with color.
-We think the landing page might be enhanced by add a dark blue or black as a primary color. Of course please feel free to try any color combination you think might work.
- We want "The Alder Circle" in large letters and "Stewards of a fair and prompt settlement" in small lettering. We don't want icons on the buttons.
- Do not want more than the one picture at top of landing page.
- We do not want any pictures that include faces. Please eliminate or replace. They will not be chosen.
- For the landing page, instead of a second set of photos please experiment with using medical symbols and legal symbols.
​
3. New Company Name: The Alder Circle
New logo is uploaded bronze and grey/silver will be colors although we are still tweaking the colors for more metallic feel. Want simple not busy.

4. The overall Web page design needs to have some website design effect (e,g image rollover, scrolling effect, hover effect etc).

5. Please follow the attached word document file for the page content of the 4 web pages. Do not mix it up.

Previous company website: www.clinjurisreview.example (we wish to convert some of the content from this website to the new brand). Competitor website that we like: www.rxboardly.example

Target Market(s)

Professional Elite. Attorneys and Doctors

Industry/Entity Type

Medical Legal

Coding

Coded - Design and coding required

Number of Pages Required

5+ page

Font styles to use
Other font styles liked:
• Helvetica or maybe font that matches logo. We are open

Colors

Designer to choose colors to be used in the design.

Requirements
Must have
• I can't locate on color scale but we want Bronze and Silver/Grey from logo. Additional colors can be added. Various shades of grey
Nice to have
• Black and white photos, simple elegant design
Should not have
• Images with faces of unknown people

```html
<!DOCTYPE html>
<html lang="en">
<head>
<meta charset="utf-8">
<title>The Alder Circle</title>
<link href="https://fonts.googleapis.com/css2?family=Open+Sans:wght@400;600;700&family=Montserrat:wght@400;500;600;700&display=swap" rel="stylesheet">
<style>
:root{
  --bronze:#b06b3c;
  --bronze-light:#e39b6c;
  --bronze-grad:linear-gradient(90deg,#a9643a,#e0996a);
  --ink:#2e2e2e;
  --text:#555;
  --pale:#f5f5f5;
  --dark:#333333;
  --dark-2:#3d3d3d;
  --footer:#262a31;
  --navy:#3b4f63;
  --blue:#2d5f9a;
  --silver-1:#d9d9d9;
  --silver-2:#9a9a9a;
}
*{box-sizing:border-box;margin:0;padding:0}
html,body{width:1200px;height:4641px;overflow:hidden}
body{font-family:"Open Sans",Arial,sans-serif;color:var(--text);background:var(--pale);position:relative}
a{color:inherit;text-decoration:none}
.abs{position:absolute}
.btn{display:inline-flex;align-items:center;justify-content:center;background:var(--bronze-grad);color:#fff;font:700 11px "Open Sans",sans-serif;letter-spacing:.5px;text-transform:uppercase;border-radius:2px}
.section-title{font:600 29px "Open Sans",sans-serif;color:var(--ink);text-align:center;letter-spacing:.3px}
.section-lead{font-size:13px;line-height:22px;text-align:center;color:var(--text);width:540px}

/* header */
.site-header{left:0;top:0;width:1200px;height:80px;background:#fff;border-bottom:1px solid #ddd}
.logo{left:120px;top:29px;display:flex;align-items:center;gap:9px;font:700 17px "Open Sans",sans-serif;color:#555;letter-spacing:.5px}
.logo-mark{width:20px;height:20px;background:var(--bronze)}
.topbar{left:402px;top:0;width:798px;height:30px;background:var(--dark);font-size:9px;color:#ddd;display:flex;align-items:center;padding-left:62px;gap:48px}
.topbar .quote{margin-left:40px;color:#fff;padding:4px 20px;background:var(--bronze-grad)}
.main-nav{left:401px;top:50px;display:flex;gap:38px;font-size:11px;color:#666}
.main-nav .active{color:var(--blue);font-weight:600}

/* hero: the single landing image */
.hero{left:0;top:80px;width:1200px;height:684px;background:radial-gradient(ellipse at 72% 35%,#8a8a8a 0%,#5a5a5a 40%,#2c2c2c 100%)}
.hero-welcome{left:112px;top:268px;font-size:12px;color:#eee;display:flex;align-items:center;gap:14px}
.hero-welcome span{display:block;width:44px;height:1px;background:#eee}
.hero-title{left:112px;top:292px;width:620px;font:700 40px/57px "Open Sans",sans-serif;color:#fff;letter-spacing:.5px}
.hero-tagline{left:112px;top:356px;font:600 18px/26px "Open Sans",sans-serif;color:#f0c3a3;letter-spacing:.3px}
.hero-copy{left:112px;top:432px;width:430px;font-size:13px;line-height:21px;color:#eee}
.hero-btn{left:112px;top:541px;width:191px;height:40px;text-transform:none}

/* why */
.why-title{left:0;top:840px;width:1200px}
.why-lead{left:330px;top:893px}
.why-card{top:971px;width:231px;height:215px;background:#fff;box-shadow:0 2px 8px rgba(0,0,0,.08);text-align:center;padding-top:30px}
.why-card svg{width:40px;height:40px}
.why-card h3{font:600 18px/26px "Open Sans",sans-serif;color:var(--ink);margin:14px 20px 10px}
.why-card p{font-size:13px;line-height:21px;color:var(--text);padding:0 26px}
.why-card.featured{background:var(--dark-2)}
.why-card.featured h3,.why-card.featured p{color:#eee}
.why-btn{left:521px;top:1225px;width:172px;height:40px}

/* medicine */
.med-band{left:283px;top:1322px;width:917px;height:467px;background:var(--dark)}
.med-panel{left:0;top:1384px;width:582px;height:449px;background:linear-gradient(135deg,var(--silver-1),var(--silver-2) 55%,#6a6a6a);display:flex;align-items:center;justify-content:center}
.med-text{left:632px;top:1412px;width:450px;color:#eee}
.med-text h2{font:600 30px "Open Sans",sans-serif;color:#fff;margin-bottom:18px}
.med-text p{font-size:13px;line-height:22px;margin-bottom:14px}
.med-text .btn{width:172px;height:38px;margin-top:14px}

/* services */
.do-title{left:0;top:1912px;width:1200px}
.do-lead{left:330px;top:1963px}
.service{top:2063px;width:321px;height:380px}
.service .panel{width:321px;height:236px;background:linear-gradient(160deg,var(--silver-1),var(--silver-2) 60%,#7a7a7a);display:flex;align-items:flex-start;justify-content:center;padding-top:62px}
.service .card{position:absolute;left:18px;top:177px;width:285px;height:203px;background:#fff;box-shadow:0 2px 10px rgba(0,0,0,.1);padding:24px 20px 0 38px}
.service h3{font:500 20px "Montserrat",sans-serif;color:var(--ink);margin-bottom:8px;white-space:nowrap}
.service p{font-size:13px;line-height:22px;color:var(--text)}
.service .more{display:block;margin-top:10px;font-size:10px;font-weight:700;color:var(--bronze);text-transform:uppercase}
.service.featured .card{background:var(--dark-2)}
.service.featured h3,.service.featured p,.service.featured .more{color:#f0f0f0}

/* consultation */
.consult-band{left:0;top:2512px;width:1200px;height:299px;background:linear-gradient(90deg,#3c3c3c,#4b4b4b 45%,#333)}
.consult{left:0;top:2548px;width:1200px;text-align:center;color:#fff}
.consult .phone{display:flex;align-items:center;justify-content:center;gap:12px;font:600 22px "Open Sans",sans-serif}
.consult h2{font:600 31px "Open Sans",sans-serif;margin:14px 0;letter-spacing:.5px}
.consult p{font-size:13px;line-height:22px;width:470px;margin:0 auto;color:#e6e6e6}
.consult .outline{display:inline-block;margin-top:24px;border:1px solid #fff;width:173px;height:39px;line-height:37px;font-size:11px;font-weight:700}

/* testimonials */
.test-title{left:0;top:2890px;width:1200px}
.test-lead{left:330px;top:2940px}
.testimonial{top:3040px;width:496px;height:258px;background:#ececec}
.testimonial .rule{position:absolute;left:61px;top:40px;width:1px;height:178px;background:var(--navy)}
.testimonial .qmark{position:absolute;left:36px;top:104px;width:50px;height:50px;border-radius:50%;background:var(--bronze);border:4px solid #f4cfb5;display:flex;align-items:center;justify-content:center;color:#fff;font:700 24px Georgia,serif}
.testimonial .stars{position:absolute;left:114px;top:38px;color:#e55b2a;font-size:15px;letter-spacing:5px}
.testimonial p{position:absolute;left:114px;top:78px;width:340px;font-size:13px;line-height:22px;color:var(--text)}
.testimonial h4{position:absolute;left:114px;top:168px;font:600 18px "Montserrat",sans-serif;color:var(--ink)}
.testimonial .place{position:absolute;left:114px;top:195px;font-size:12px;color:var(--text)}
.testimonial .badge{position:absolute;left:400px;top:160px;width:58px;height:58px;border-radius:50%;background:linear-gradient(135deg,#c9c9c9,#8a8a8a)}
.dots{left:565px;top:3339px;display:flex;gap:10px}
.dots span{width:10px;height:10px;border-radius:50%;background:#ccc}
.dots .on{background:#fff;border:2px solid var(--bronze)}

/* contact */
.contact-bg{left:0;top:3388px;width:1200px;height:760px;background:#fff}
.contact-title{left:0;top:3444px;width:1200px}
.contact-lead{left:330px;top:3496px}
.contact-box{left:92px;top:3597px;width:1013px;height:459px;background:#f6f6f6}
.contact-panel{left:92px;top:3597px;width:510px;height:459px;background:linear-gradient(135deg,#425a70,#34495e)}
.contact-info{left:177px;top:3663px;color:#fff}
.contact-info h4{font:600 16px "Open Sans",sans-serif;margin-bottom:22px}
.contact-info .call{font-size:22px;margin-bottom:6px}
.contact-info .small{font-size:12px;line-height:19px}
.contact-info .block{margin-top:24px}
.socials{display:flex;gap:10px;margin-top:54px}
.socials span{width:32px;height:32px;border-radius:50%;border:1px solid rgba(255,255,255,.5);background:rgba(255,255,255,.12)}
.socials span.on{background:#fff}
.form{left:687px;top:3660px;width:333px}
.form h4{font:600 17px "Open Sans",sans-serif;color:var(--blue);margin-bottom:24px}
.field{height:34px;background:#f2f2f2;border:1px solid #e8e8e8;margin-bottom:16px;font-size:10px;color:#888;padding:10px 14px}
.field.msg{height:94px}
.form .btn{width:110px;height:38px;margin-top:8px}

/* footer */
.footer{left:0;top:4190px;width:1200px;height:451px;background:var(--footer)}
.info-bar{left:67px;top:4141px;width:1068px;height:103px;background:var(--bronze-grad);border-radius:3px;display:flex;align-items:center;padding-left:40px;color:#fff}
.info-item{display:flex;align-items:center;gap:18px;width:357px}
.info-item h5{font:600 17px "Open Sans",sans-serif;margin-bottom:6px}
.info-item span{font-size:12px}
.fcol{top:4315px;color:#ddd}
.fcol h5{font:600 18px "Open Sans",sans-serif;color:#fff;margin-bottom:14px}
.fcol .bar{width:32px;height:2px;background:#fff;margin-bottom:26px}
.fcol p{font-size:13px;line-height:29px}
.fcol .read{font-size:15px;color:var(--bronze-light);text-decoration:underline;display:block;margin-top:14px}
.links{display:grid;grid-template-columns:178px 120px;row-gap:12px;font-size:13px;color:#eee}
.links a{text-decoration:underline}
.subscribe{display:flex;margin-top:22px}
.subscribe .in{width:276px;height:53px;background:#fff;border-radius:4px 0 0 4px;font-size:12px;color:#333;padding:18px 16px}
.subscribe .go{width:63px;height:53px;background:var(--bronze-grad);border-radius:0 4px 4px 0;display:flex;align-items:center;justify-content:center}
.bottom-bar{left:0;top:4577px;width:1200px;height:64px;border-top:1px solid #3a3f47}
.foot-logo{left:65px;top:4567px;width:173px;height:74px;background:var(--bronze-grad);display:flex;align-items:center;justify-content:center;gap:8px;color:#fff;font:700 14px "Open Sans",sans-serif}
.foot-logo i{width:14px;height:14px;background:#fff;display:block}
.foot-social{left:898px;top:4577px;display:flex;border-right:1px solid #3a3f47}
.foot-social span{width:59px;height:64px;border-left:1px solid #3a3f47;display:flex;align-items:center;justify-content:center}
.foot-social span i{width:10px;height:10px;border-radius:50%;background:#555c66;display:block}
</style>
</head>
<body>

<header class="site-header abs">
  <div class="abs logo"><span class="logo-mark"></span>THE ALDER CIRCLE</div>
  <div class="abs topbar">
    <span>&#9679; 48 Linden Row, Easton, NY 10420</span>
    <span>Follow Us: &#9679; &#9679; &#9679;</span>
    <span class="quote">GET QUOTATION</span>
  </div>
  <nav class="abs main-nav">
    <a class="active">Home</a><a>About Us</a><a>Services</a><a>Stakeholders</a><a>QME Physicians</a><a>Member Physicians</a>
  </nav>
</header>

<section class="abs hero" role="img" aria-label="Black and white photo of a physician in scrubs with a stethoscope, no visible face"></section>
<div class="abs hero-welcome">Welcome <span></span></div>
<h1 class="abs hero-title">The Alder Circle</h1>
<p class="abs hero-tagline">Stewards of a fair and prompt settlement</p>
<p class="abs hero-copy">Lorem ipsum dolor sit amet, consectetur adipiscing elit, sed do eiusmod tempor incididunt ut labore et dolore magna Lorem ipsum dolor sit amet, consectetur adipiscing elit, sed do eiusmod tempor incididunt ut labore et dolore magna</p>
<a class="abs btn hero-btn">Discover more</a>

<h2 class="abs section-title why-title">Why We AreThe Best</h2>
<p class="abs section-lead why-lead">Lorem ipsum dolor sit amet, consectetur adipiscing elit, sed do eiusmod tempor incididunt ut labore et dolore magna aliqua. Ut enim ad min</p>

<div class="abs why-card" style="left:94px">
  <svg viewBox="0 0 40 40" fill="none" stroke="#b06b3c" stroke-width="1.6"><circle cx="20" cy="20" r="6"/><path d="M20 6l3 5 6-1 1 6 5 3-4 5 2 6-6 1-3 5-5-3-5 3-3-5-6-1 2-6-4-5 5-3 1-6 6 1z"/></svg>
  <h3>Expertise</h3><p>Lorem ipsum dolor sit amet, consectetur adipiscing</p>
</div>
<div class="abs why-card featured" style="left:353px">
  <svg viewBox="0 0 40 40" fill="none" stroke="#eee" stroke-width="1.6"><circle cx="18" cy="18" r="12"/><path d="M6 18h24M18 6c-5 6-5 18 0 24M18 6c5 6 5 18 0 24"/><circle cx="28" cy="28" r="5" fill="#3d3d3d"/></svg>
  <h3>Comprehensive Services</h3><p>Lorem ipsum dolor sit amet, consectetur adipiscing</p>
</div>
<div class="abs why-card" style="left:613px">
  <svg viewBox="0 0 40 40" fill="none" stroke="#b06b3c" stroke-width="1.6"><circle cx="20" cy="13" r="7"/><path d="M7 35c0-8 6-13 13-13s13 5 13 13z"/></svg>
  <h3>Experienced</h3><p>Lorem ipsum dolor sit amet, consectetur adipiscing</p>
</div>
<div class="abs why-card" style="left:874px">
  <svg viewBox="0 0 40 40" fill="none" stroke="#b06b3c" stroke-width="1.6"><path d="M20 5l4.5 9.5 10.5 1.5-7.5 7.3 1.8 10.4L20 28.8l-9.3 4.9 1.8-10.4L5 16l10.5-1.5z"/></svg>
  <h3>Unbiased Evaluation</h3><p>Lorem ipsum dolor sit amet, consectetur adipiscing</p>
</div>
<a class="abs btn why-btn">Learn more about</a>

<div class="abs med-band"></div>
<div class="abs med-panel">
  <svg width="120" height="120" viewBox="0 0 120 120" fill="none" stroke="#fff" stroke-width="3" opacity=".8"><circle cx="60" cy="60" r="56"/><path d="M50 28h20v22h22v20H70v22H50V70H28V50h22z"/></svg>
</div>
<div class="abs med-text">
  <h2>Medicine for Legal Insight</h2>
  <p>Lorem ipsum dolor sit amet, consectetur adipiscing elit, sed do eiusmod tempor incididunt ut labore et dolore magna aliqua. Ut enim ad minim veniam, quis nostrud ex</p>
  <p>Lorem ipsum dolor sit amet, consectetur adipiscing elit, sed do eiusmod tempor incididunt ut labore et dolore magna aliqua. Ut enim ad minim veniam, quis nostrud exercitation ullamco laboris nisi ut aliquip ex ea commodo consequat. Duis aute iru</p>
  <a class="btn">Learn more about</a>
</div>

<h2 class="abs section-title do-title">What We Do</h2>
<p class="abs section-lead do-lead">Lorem ipsum dolor sit amet, consectetur adipiscing elit, sed do eiusmod tempor incididunt ut labore et dolore magna aliqua. Ut enim ad min</p>

<article class="abs service" style="left:94px">
  <div class="panel"><svg width="60" height="60" viewBox="0 0 60 60" fill="none" stroke="#fff" stroke-width="2.4"><path d="M24 8h12v16h16v12H36v16H24V36H8V24h16z"/></svg></div>
  <div class="card"><h3>Medical Examinations</h3><p>Lorem ipsum dolor sit amet, cons ectetur adipiscing elit, sed do eius mod tempor incididunt ut labore et dolore magna aliqua.</p><a class="more">Learn more</a></div>
</article>
<article class="abs service featured" style="left:440px">
  <div class="panel"><svg width="60" height="60" viewBox="0 0 60 60" fill="none" stroke="#fff" stroke-width="2.4"><path d="M30 8v44M18 52h24M10 16h40M10 16l-6 16h12zM50 16l-6 16h12z"/></svg></div>
  <div class="card"><h3>Expert Testimony</h3><p>Lorem ipsum dolor sit amet, cons ectetur adipiscing elit, sed do eius mod tempor incididunt ut labore et dolore magna aliqua.</p><a class="more">Learn more</a></div>
</article>
<article class="abs service" style="left:787px">
  <div class="panel"><svg width="60" height="60" viewBox="0 0 60 60" fill="none" stroke="#fff" stroke-width="2.4"><rect x="12" y="6" width="36" height="48" rx="2"/><path d="M20 20h20M20 30h20M20 40h12"/></svg></div>
  <div class="card"><h3>Medical Records</h3><p>Lorem ipsum dolor sit amet, cons ectetur adipiscing elit, sed do eius mod tempor incididunt ut labore et dolore magna aliqua.</p><a class="more">Learn more</a></div>
</article>

<div class="abs consult-band"></div>
<div class="abs consult">
  <div class="phone">
    <svg width="34" height="34" viewBox="0 0 34 34" fill="none" stroke="#fff" stroke-width="1.6"><path d="M8 3l5 7-3 3c2 5 6 9 11 11l3-3 7 5-3 5C16 31 3 18 3 6z"/></svg>
    123-456-7890
  </div>
  <h2>Get Free Consultation Today</h2>
  <p>Lorem ipsum dolor sit amet, consectetur adipiscing elit, sed do eiusmod tempor incididunt ut labore et dolore magna aliqua.</p>
  <a class="outline">CONTACT US NOW</a>
</div>

<h2 class="abs section-title test-title">Client Testimonials</h2>
<p class="abs section-lead test-lead">Lorem ipsum dolor sit amet, consectetur adipiscing elit, sed do eiusmod tempor incididunt ut labore et dolore magna aliqua. Ut enim ad min</p>

<article class="abs testimonial" style="left:90px">
  <span class="rule"></span><span class="qmark">&rdquo;</span><span class="stars">&#9733;&#9733;&#9733;&#9733;&#9733;</span>
  <p>Lorem ipsum dolor sit amet, consectetur adipiscing elit, sed do eiusmod tempor incididunt ut labore et dolore magna aliqua. Ut enim</p>
  <h4>Maren Holt</h4><span class="place">Birch Hollow</span>
  <span class="badge"></span>
</article>
<article class="abs testimonial" style="left:611px">
  <span class="rule"></span><span class="qmark">&rdquo;</span><span class="stars">&#9733;&#9733;&#9733;&#9733;&#9733;</span>
  <p>Lorem ipsum dolor sit amet, consectetur adipiscing elit, sed do eiusmod tempor incididunt ut labore et dolore magna aliqua. Ut enim</p>
  <h4>Maren Holt</h4><span class="place">Birch Hollow</span>
  <span class="badge"></span>
</article>
<div class="abs dots"><span></span><span></span><span class="on"></span><span></span></div>

<div class="abs contact-bg"></div>
<h2 class="abs section-title contact-title">Contact Us</h2>
<p class="abs section-lead contact-lead">Lorem ipsum dolor sit amet, consectetur adipiscing elit, sed do eiusmod tempor incididunt ut labore et dolore magna aliqua. Ut enim ad min</p>
<div class="abs contact-box"></div>
<div class="abs contact-panel"></div>
<div class="abs contact-info">
  <h4>CONTACT US</h4>
  <div class="call">Call: 0123456789</div>
  <div class="small">info@company.com</div>
  <div class="small block">Address:<br>SOME PLACE<br>51100 Road</div>
  <div class="small block">Operating Hours<br>Monday to Saturday: 9:00 - 18:00<br>Sunday: Closed</div>
  <div class="socials"><span></span><span class="on"></span><span></span><span></span></div>
</div>
<form class="abs form">
  <h4>FREE CONSULTATION</h4>
  <div class="field">Your Name</div>
  <div class="field">Email</div>
  <div class="field">Phone</div>
  <div class="field msg">Message ...</div>
  <a class="btn">Submit</a>
</form>

<footer class="abs footer"></footer>
<div class="abs info-bar">
  <div class="info-item">
    <svg width="52" height="46" viewBox="0 0 52 46" fill="none" stroke="#fff" stroke-width="1.6"><path d="M26 30c-7-9-10-14-10-19a10 10 0 0120 0c0 5-3 10-10 19z"/><circle cx="26" cy="11" r="4"/><path d="M14 26L3 43h46L38 26"/></svg>
    <div><h5>Address</h5><span>185, Los Angeles, USA</span></div>
  </div>
  <div class="info-item">
    <svg width="48" height="48" viewBox="0 0 34 34" fill="none" stroke="#fff" stroke-width="1.4"><path d="M8 3l5 7-3 3c2 5 6 9 11 11l3-3 7 5-3 5C16 31 3 18 3 6z"/></svg>
    <div><h5>Phone</h5><span>+123 456 78890</span></div>
  </div>
  <div class="info-item">
    <svg width="46" height="46" viewBox="0 0 46 46" fill="none" stroke="#fff" stroke-width="1.6"><path d="M4 18l19-14 19 14v24H4z"/><path d="M4 18l19 14 19-14"/><rect x="12" y="10" width="22" height="16"/></svg>
    <div><h5>Email Contact</h5><span>info@company.com</span></div>
  </div>
</div>

<div class="abs fcol" style="left:67px;width:300px">
  <h5>About Us</h5><div class="bar"></div>
  <p>Lorem ipsum dolor sit amet, consectetur adipi elit, sed do eiusmod tempor incididunt ut lab dolore magna aliqua.</p>
  <a class="read">Read More</a>
</div>
<div class="abs fcol" style="left:434px">
  <h5>Useful Links</h5><div class="bar"></div>
  <div class="links"><a>About Us</a><a>Services</a><a>Projects</a><a>Shop</a><a>Blog</a><a>Privacy Policy</a><a>Contact Us</a><a>Help Desk</a></div>
</div>
<div class="abs fcol" style="left:798px;width:340px">
  <h5>Useful Links</h5><div class="bar"></div>
  <p style="line-height:24px">If you have any questions, Subscribe to our newsletter to get our latest products</p>
  <div class="subscribe"><div class="in">Email</div><div class="go"><svg width="20" height="20" viewBox="0 0 20 20" fill="none" stroke="#fff" stroke-width="1.6"><path d="M3 10h14M11 4l6 6-6 6"/></svg></div></div>
</div>

<div class="abs bottom-bar"></div>
<div class="abs foot-logo"><i></i>THE ALDER CIRCLE</div>
<div class="abs foot-social"><span><i></i></span><span><i></i></span><span><i></i></span><span><i></i></span></div>

</body>
</html>
```